Business Card Design

We require a business card design for a law firm, our signature colours are maroon and cream. Our slogan is "From our family to yours", we would like the cards to be professional however feminine at the same time.

Industry/Entity Type

Business

Contact Information for Business Card

Helena Brackett & Associates Lawyers & Conveyancers, Helena Brackett LL.B. Principal Solicitor, 17 Quillon Street, Marrowdale NSW 2190

Logo styles of interest
Emblem Logo
Abstract Logo
Wordmark Logo

```html
<!DOCTYPE html>
<html lang="en">
<head>
<meta charset="utf-8">
<title>Helena Brackett &amp; Associates – Business Card</title>
<link rel="stylesheet" href="https://fonts.googleapis.com/css2?family=EB+Garamond:wght@400;500;600&display=swap">
<style>
  :root {
    --maroon: #8e2a35;
    --paper: #ffffff;
    --on-maroon: #fbf6ef;
    --emblem-light: #c98f96;
  }
  html, body {
    margin: 0;
    padding: 0;
    overflow: hidden;
    background: var(--paper);
  }
  .card {
    position: relative;
    width: 1200px;
    height: 695px;
    background: var(--paper);
    font-family: "EB Garamond", Garamond, "Times New Roman", serif;
    color: var(--maroon);
    overflow: hidden;
  }
  .frame {
    position: absolute;
    left: 0;
    top: 0;
  }
  .emblem {
    position: absolute;
    left: 478px;
    top: 30px;
    width: 226px;
    height: 196px;
    border-radius: 50% 50% 40% 40%;
    background: radial-gradient(ellipse at 50% 45%, var(--maroon) 0%, var(--emblem-light) 75%, transparent 100%);
    opacity: 0.85;
  }
  .firm-name {
    position: absolute;
    left: 0;
    width: 1200px;
    top: 258px;
    margin: 0;
    text-align: center;
    font-weight: 600;
    font-size: 49px;
    line-height: 70px;
    letter-spacing: 0.2px;
  }
  .slogan {
    position: absolute;
    left: 0;
    width: 1200px;
    top: 424px;
    margin: 0;
    text-align: center;
    font-weight: 400;
    font-size: 29px;
    letter-spacing: 0.6px;
    text-transform: uppercase;
  }
  .contact-band {
    position: absolute;
    left: 40px;
    top: 518px;
    width: 1118px;
    height: 134px;
    background: var(--maroon);
    color: var(--on-maroon);
  }
  .person-name {
    position: absolute;
    left: 48px;
    top: 20px;
    margin: 0;
    font-weight: 600;
    font-size: 37px;
  }
  .person-role {
    position: absolute;
    left: 48px;
    top: 78px;
    margin: 0;
    font-weight: 400;
    font-size: 32px;
  }
  .address {
    position: absolute;
    right: 40px;
    top: 86px;
    margin: 0;
    font-weight: 400;
    font-size: 25px;
    font-style: normal;
  }
</style>
</head>
<body>
  <main class="card">
    <svg class="frame" width="1200" height="695" viewBox="0 0 1200 695" aria-hidden="true">
      <g fill="none" stroke="var(--maroon)" stroke-width="3">
        <polyline points="424,48 41.5,48 41.5,520"/>
        <polyline points="742,48 1156.5,48 1156.5,520"/>
      </g>
    </svg>

    <div class="emblem" role="img" aria-label="Firm emblem: scales of justice with decorative scrolls"></div>

    <h1 class="firm-name">Helena Brackett &amp; Associates<br>Lawyers &amp; Conveyancers</h1>
    <p class="slogan">From our family to yours</p>

    <section class="contact-band">
      <p class="person-name">Helena Brackett LL.B.</p>
      <p class="person-role">Principal Solicitor</p>
      <address class="address">17 Quillon Street, Marrowdale NSW 2190</address>
    </section>
  </main>
</body>
</html>
```